Predictive Analytics User Interface

We need a User Interface for web application to be used by School District administrators in the United States. The software is a Predictive Analytics application that will allow a school district administrators to see Predictions of how a campus will perform in the following categories:

State Assessment Exams (example: Will a specific grade level (3rd, 4th, 5th, etc.) achieve their target test scores in May, 2017)
Graduation Rates (example: Will the 12th grade class graduation rate achieve their goal of 98% graduation rate by May, 2017)
Drop-Out Rates (example: Will the current 9th grade class have a drop-out rate lower than 5% in the next four years (assuming it takes all 9th graders 4 years to graduate from US high schools).

We are looking for sleek but simple. The design must support the data - not detract from it.

Target Market(s)

Public Education in Grades 1-12 and Higher Education for 2-year and 4-year colleges.

Industry/Entity Type

Education

Number of Pages Required

3 page

Font styles to use
Sans Serif

Colors
f78f20
9bcb3c
ec1f27
6b449b
0455a3

Requirements
Must have
• Ability to segment student groups into four probability categories: Excellent, Good, Fair, and Poor. Additionally, each student group should have "Action Buttons" that show an activity for each student group. For example, let's say a School Principal looks at their screen and clicks on High School Graduation. They would get students in four groups. If the "Poor" category showed 12% of the school, the Principal would have "Action Buttons" like "Assign to Tutoring" or "Meet with Counselor" to address their needs. The goal is not just to identify student groups but also be able to take action directly from the UI.
Nice to have
• Drill-down capabilities in each group that shows me deeper details. For example, if a School Principal looked at the High School Graduation section and clicked on "Poor" which showed a Student Group with low probability of graduating from high school, it would be nice if the principal could click on a "See Details" and see another layer of data explaining why the Prediction believes these students will drop out. As an example, it could show a report of 10+ absences, 15+ behavior issues reported, and failing 2 classes. It could also show recommendations as to improve their probability with different interventions like "sign up for tutoring" or "assign a mentor".
Should not have
• Small print, small charts and colors difficult to read. Our target audience is people between the age of 50-70, so their eyesight is not always the best. We are looking for simple and clean but bold enough that your grandmother could view it and have a discussion about the data.

```html
<!DOCTYPE html>
<html lang="en">
<head>
<meta charset="utf-8">
<title>Kestrel – Dashboard</title>
<link href="https://fonts.googleapis.com/css2?family=Montserrat:wght@300;400;500;600;700&display=swap" rel="stylesheet">
<style>
:root{
  --red:#ec1f27;--orange:#f78f20;--green:#9bcb3c;--purple:#6b449b;--blue:#0455a3;
  --sky:#3aa8d8;--side:#153848;--ink:#222;--muted:#666;--line:#e3e3e3;--bg:#fafafa;
}
*{margin:0;padding:0;box-sizing:border-box}
html,body{width:1200px;height:826px;overflow:hidden}
body{font-family:"Montserrat",sans-serif;color:var(--ink);background:var(--bg);position:relative}
.abs{position:absolute}
.header{left:0;top:0;width:1200px;height:69px;background:#fff}
.brand{left:48px;top:14px;font-size:34px;font-weight:700;color:#1c4a57;letter-spacing:2px;line-height:34px}
.tools{left:855px;top:24px;display:flex;gap:18px;align-items:center}
.tools svg{display:block}
.divider{left:1035px;top:10px;width:1px;height:50px;background:var(--line)}
.avatar{left:1055px;top:18px;width:31px;height:31px;border-radius:50%;background:linear-gradient(135deg,#8a5a44,#d9a88a)}
.user{left:1094px;top:18px;font-size:14px;color:var(--blue);font-weight:500;line-height:16px}
.user small{display:block;font-size:11px;color:var(--muted);font-weight:400}
.sidebar{left:0;top:84px;width:223px;height:742px;background:var(--side)}
.nav-item{position:absolute;left:0;width:223px;height:43px;display:flex;align-items:center;color:#fff;font-weight:600;font-size:13px}
.nav-item.active{background:var(--sky)}
.nav-item.active::after{content:"";position:absolute;right:0;top:15px;border:6px solid transparent;border-right-color:var(--bg)}
.nav-icon{width:29px;height:29px;border-radius:50%;background:#fff;margin:0 9px 0 48px;display:flex;align-items:center;justify-content:center}
.stat{top:84px;width:223px;height:51px;background:#fff;border:1px solid var(--line);display:flex}
.stat .face{width:51px;height:51px;display:flex;align-items:center;justify-content:center;margin:-1px 0 0 -1px}
.stat .val{font-size:24px;font-weight:300;line-height:24px;margin:9px 0 0 16px}
.stat .lbl{font-size:10.5px;font-weight:500;color:#333;letter-spacing:.2px}
.tabs{left:240px;top:180px;width:942px;height:36px;background:#fff;border:1px solid var(--line);font-size:12.5px;display:flex;align-items:center}
.tab{display:flex;align-items:center;gap:9px;height:100%;padding:0 12px 0 15px}
.tab.on{border-bottom:2px solid #999}
.card{background:#fff;border:1px solid var(--line)}
.card svg{display:block}
.action{top:705px;width:239px;height:59px;background:#fff;border:1px solid var(--line);display:flex;align-items:center;font-size:15.5px;font-weight:500}
.action .ico{width:53px;height:59px;background:var(--blue);margin:-1px 16px 0 -1px;display:flex;align-items:center;justify-content:center}
.foot{left:240px;top:792px;font-size:11px}
</style>
</head>
<body>
<header class="abs header">
  <div class="abs brand">Kestrel</div>
  <div class="abs tools">
    <svg width="20" height="20" viewBox="0 0 20 20"><circle cx="10" cy="10" r="9.5"/><rect x="8.8" y="4" width="2.4" height="8" fill="#fff"/><circle cx="10" cy="15" r="1.3" fill="#fff"/></svg>
    <svg width="18" height="18" viewBox="0 0 18 18" fill="#222"><circle cx="9" cy="5" r="4"/><path d="M2 17c0-5 3-7 7-7s7 2 7 7z"/></svg>
    <svg width="18" height="20" viewBox="0 0 18 20"><path d="M9 3c-3 0-5 2-5 5v4l-2 3h14l-2-3V8c0-3-2-5-5-5z" fill="#222"/><circle cx="9" cy="17.5" r="2" fill="#222"/><circle cx="13" cy="4" r="4" fill="var(--orange)"/></svg>
    <svg width="22" height="18" viewBox="0 0 22 18"><rect x="1" y="5" width="17" height="12" fill="none" stroke="#222" stroke-width="2"/><path d="M1 5l8.5 7L18 5" fill="none" stroke="#222" stroke-width="2"/><circle cx="17" cy="4" r="4" fill="var(--red)"/></svg>
    <svg width="22" height="18" viewBox="0 0 22 18" fill="#111"><rect y="1" width="22" height="3"/><rect y="7.5" width="22" height="3"/><rect y="14" width="22" height="3"/></svg>
  </div>
  <div class="abs divider"></div>
  <div class="abs avatar" role="img" aria-label="User profile photo"></div>
  <div class="abs user">Lorem ipsum<small>HR Admin</small></div>
</header>

<nav class="abs sidebar">
  <div class="nav-item active" style="top:0"><span class="nav-icon"><svg width="14" height="14" viewBox="0 0 14 14" fill="var(--side)"><path d="M7 1L0 7h2v6h4V9h2v4h4V7h2z"/></svg></span>Dashboard</div>
  <div class="nav-item" style="top:51px"><span class="nav-icon"><svg width="14" height="14" viewBox="0 0 14 14"><circle cx="5" cy="8" r="4" fill="none" stroke="var(--side)" stroke-width="3" stroke-dasharray="2 1.2"/><circle cx="11" cy="4" r="2.3" fill="var(--side)"/></svg></span>Settings</div>
  <div class="nav-item" style="top:103px"><span class="nav-icon"><svg width="16" height="14" viewBox="0 0 16 14" fill="var(--side)"><circle cx="4" cy="4" r="2.5"/><circle cx="12" cy="4" r="2.5"/><circle cx="8" cy="6" r="2.5"/><path d="M1 12c0-3 2-4 3-4s3 1 3 4zM9 12c0-3 2-4 3-4s3 1 3 4zM4 13c0-3 2-4 4-4s4 1 4 4z"/></svg></span>Academic</div>
  <div class="nav-item" style="top:154px"><span class="nav-icon"><svg width="16" height="12" viewBox="0 0 16 12"><path d="M1 6c3-5 11-5 14 0-3 5-11 5-14 0z" fill="var(--side)"/><circle cx="8" cy="6" r="2.5" fill="#fff"/></svg></span>HR/Payroll</div>
  <div class="nav-item" style="top:206px"><span class="nav-icon"><svg width="12" height="14" viewBox="0 0 12 14" fill="var(--side)"><circle cx="6" cy="4" r="3.5"/><path d="M0 14c0-4 2-6 6-6s6 2 6 6z"/></svg></span>Student</div>
  <div class="nav-item" style="top:257px"><span class="nav-icon"><svg width="16" height="11" viewBox="0 0 16 11"><rect width="16" height="11" fill="var(--side)"/><circle cx="8" cy="5.5" r="2.5" fill="#fff"/></svg></span>Finance</div>
  <div class="nav-item" style="top:309px"><span class="nav-icon"><svg width="12" height="14" viewBox="0 0 12 14" fill="var(--side)"><path d="M3 0h9v11H3a1.5 1.5 0 000 3h9v-1.5H3z"/><path d="M1 2l2-2v11l-2 2z"/></svg></span>Library</div>
  <div class="nav-item" style="top:360px"><span class="nav-icon"><svg width="16" height="12" viewBox="0 0 16 12" fill="var(--side)"><rect width="10" height="9"/><path d="M10 3h3l3 3v3h-6z"/><circle cx="4" cy="10" r="2"/><circle cx="12" cy="10" r="2"/></svg></span>Transport</div>
  <div class="nav-item" style="top:411px"><span class="nav-icon"><svg width="16" height="12" viewBox="0 0 16 12" fill="var(--side)"><rect y="1" width="2" height="11"/><rect y="7" width="16" height="3"/><circle cx="5" cy="5" r="2"/><rect x="8" y="3" width="8" height="4"/><rect x="14" y="7" width="2" height="5"/></svg></span>Hostel</div>
  <div class="nav-item" style="top:463px"><span class="nav-icon"><svg width="15" height="11" viewBox="0 0 15 11"><rect width="15" height="11" rx="1" fill="var(--side)"/><path d="M0 1l7.5 5L15 1" fill="none" stroke="#fff" stroke-width="1.4"/></svg></span>Messages/SMS</div>
  <div class="nav-item" style="top:514px"><span class="nav-icon"><svg width="14" height="12" viewBox="0 0 14 12" fill="var(--side)"><rect width="3" height="3"/><rect x="4" width="10" height="3"/><rect y="4.5" width="3" height="3"/><rect x="4" y="4.5" width="10" height="3"/><rect y="9" width="3" height="3"/><rect x="4" y="9" width="10" height="3"/></svg></span>Store Management</div>
</nav>

<div class="abs stat" style="left:240px"><div class="face" style="background:var(--red)"><svg width="36" height="36" viewBox="0 0 36 36" fill="none" stroke="#fff" stroke-width="2"><circle cx="18" cy="18" r="16"/><circle cx="12.5" cy="14" r="1.2" fill="#fff"/><circle cx="23.5" cy="14" r="1.2" fill="#fff"/><path d="M11 26c4-5 10-5 14 0"/></svg></div><div><div class="val" style="color:var(--red)">250</div><div class="lbl" style="margin-left:16px">POOR STUDENTS</div></div></div>
<div class="abs stat" style="left:483px"><div class="face" style="background:var(--orange)"><svg width="36" height="36" viewBox="0 0 36 36" fill="none" stroke="#fff" stroke-width="2"><circle cx="18" cy="18" r="16"/><circle cx="12.5" cy="14" r="1.2" fill="#fff"/><circle cx="23.5" cy="14" r="1.2" fill="#fff"/><path d="M12 23h12"/></svg></div><div><div class="val" style="color:var(--orange)">375</div><div class="lbl" style="margin-left:16px">FAIR STUDENTS</div></div></div>
<div class="abs stat" style="left:716px"><div class="face" style="background:var(--green)"><svg width="36" height="36" viewBox="0 0 36 36" fill="none" stroke="#fff" stroke-width="2"><circle cx="18" cy="18" r="16"/><circle cx="12.5" cy="14" r="1.2" fill="#fff"/><circle cx="23.5" cy="14" r="1.2" fill="#fff"/><path d="M11 21c4 5 10 5 14 0"/></svg></div><div><div class="val" style="color:var(--green)">758</div><div class="lbl" style="margin-left:16px">GOOD STUDENTS</div></div></div>
<div class="abs stat" style="left:959px"><div class="face" style="background:var(--blue)"><svg width="36" height="36" viewBox="0 0 36 36" fill="none" stroke="#fff" stroke-width="2"><circle cx="18" cy="18" r="16"/><circle cx="12.5" cy="14" r="1.2" fill="#fff"/><circle cx="23.5" cy="14" r="1.2" fill="#fff"/><path d="M10 20c4 7 12 7 16 0"/></svg></div><div><div class="val" style="color:var(--blue)">1520</div><div class="lbl" style="margin-left:16px">EXCELLENT</div></div></div>

<div class="abs tabs">
  <div class="tab on"><svg width="13" height="10" viewBox="0 0 13 10" fill="#222"><rect width="13" height="1.6"/><rect y="4.2" width="13" height="1.6"/><rect y="8.4" width="13" height="1.6"/></svg>Activity</div>
  <div class="tab"><svg width="13" height="13" viewBox="0 0 13 13" fill="none" stroke="#333"><rect x=".5" y="1.5" width="12" height="11"/><path d="M.5 4.5h12M3 0v3M10 0v3M3 7h1M6 7h1M9 7h1M3 10h1M6 10h1M9 10h1"/></svg>Schedule</div>
  <div class="tab"><svg width="13" height="13" viewBox="0 0 13 13" fill="none" stroke="#333"><rect x=".5" y="1.5" width="12" height="11"/><path d="M.5 4.5h12M3 0v3M10 0v3M3 7h1M6 7h1M9 7h1M3 10h1M6 10h1M9 10h1"/></svg>Fee reports</div>
  <div style="margin-left:auto;display:flex;align-items:center;gap:10px;padding-right:26px"><svg width="14" height="14" viewBox="0 0 14 14" fill="#333"><rect width="3.5" height="3.5"/><rect x="5.2" width="3.5" height="3.5"/><rect x="10.4" width="3.5" height="3.5"/><rect y="5.2" width="3.5" height="3.5"/><rect x="5.2" y="5.2" width="3.5" height="3.5"/><rect x="10.4" y="5.2" width="3.5" height="3.5"/><rect y="10.4" width="3.5" height="3.5"/><rect x="5.2" y="10.4" width="3.5" height="3.5"/><rect x="10.4" y="10.4" width="3.5" height="3.5"/></svg><svg width="8" height="5" viewBox="0 0 8 5" fill="none" stroke="#555"><path d="M1 1l3 3 3-3"/></svg></div>
  <div style="display:flex;align-items:center;gap:8px;padding-right:14px"><svg width="14" height="13" viewBox="0 0 14 13" fill="none" stroke="#333"><rect x="3.5" y=".5" width="10" height="10"/><path d="M.5 3.5v9h10M6 3.5h5M6 5.5h5M6 7.5h5"/></svg>Support</div>
</div>

<section class="abs card" style="left:240px;top:236px;width:505px;height:445px">
<svg width="505" height="445" viewBox="0 0 589 520" font-family="Montserrat,sans-serif">
  <text x="18" y="47" font-size="14" fill="#222">Daily Attendance Overview</text>
  <path d="M534 40l5 5 5-5" fill="none" stroke="#333" stroke-width="1.6"/>
  <path d="M566 39a5 5 0 10 1 6M566 36v4h-4" fill="none" stroke="#333" stroke-width="1.6"/>
  <g font-size="11.5" font-weight="500" fill="#444">
    <rect x="20" y="81" width="4" height="19" fill="var(--purple)"/><text x="30" y="96">SECONDARY</text>
    <rect x="143" y="81" width="4" height="19" fill="var(--sky)"/><text x="153" y="96">HIGHER</text>
    <rect x="239" y="81" width="4" height="19" fill="var(--orange)"/><text x="249" y="96">COLLEGE</text>
  </g>
  <g stroke="#ececec">
    <path d="M62 147h496M62 195h496M62 244h496M62 291h496M62 339h496M62 386h496"/>
    <path d="M150 137v297M232 137v297M307 137v297M387 137v297M470 137v297M547 137v297"/>
  </g>
  <path d="M70 137v297h488" fill="none" stroke="#ccc"/>
  <g font-size="14" fill="#555" text-anchor="end">
    <text x="52" y="152">30</text><text x="52" y="200">25</text><text x="52" y="249">20</text><text x="52" y="296">15</text><text x="52" y="344">10</text><text x="48" y="391">5</text><text x="48" y="439">0</text>
  </g>
  <g font-size="14" fill="#555" text-anchor="middle">
    <text x="70" y="459">18/12</text><text x="151" y="459">19/12</text><text x="232" y="459">20/12</text><text x="307" y="459">21/12</text><text x="387" y="459">22/12</text><text x="470" y="459">Today</text><text x="547" y="459">24/12</text>
  </g>
  <g fill="none" stroke-width="1.2">
    <polyline stroke="var(--sky)" points="71,170 150,265 237,170 395,370 515,260"/>
    <polyline stroke="var(--orange)" points="71,281 148,155 230,245 275,231 317,311 406,281 435,174 513,192"/>
    <polyline stroke="var(--purple)" points="71,339 143,213 228,340 357,182 515,247"/>
  </g>
</svg>
</section>

<section class="abs card" style="left:771px;top:236px;width:197px;height:248px">
<svg width="197" height="248" viewBox="0 0 230 290" font-family="Montserrat,sans-serif">
  <text x="115" y="38" font-size="22" text-anchor="middle" fill="#333">Graduation Rates</text>
  <path d="M116 131L55.3 102.7A67 67 0 0 1 144.3 70.3z" fill="var(--sky)"/>
  <path d="M116 131L144.3 70.3A67 67 0 0 1 148.5 189.6z" fill="var(--orange)"/>
  <path d="M116 131L148.5 189.6A67 67 0 0 1 55.3 102.7z" fill="var(--purple)"/>
  <g fill="#fff" font-size="20" text-anchor="middle"><text x="120" y="102">25</text><text x="149" y="153">35</text><text x="89" y="153">40%</text></g>
  <g font-size="11.5" font-weight="500" fill="#444">
    <rect x="19" y="233" width="4" height="13" fill="var(--purple)"/><text x="28" y="243">SECONDARY</text>
    <rect x="137" y="233" width="4" height="13" fill="var(--orange)"/><text x="146" y="244">COLLEGE</text>
    <rect x="19" y="260" width="4" height="13" fill="var(--sky)"/><text x="28" y="270">HIGHER</text>
  </g>
</svg>
</section>

<section class="abs card" style="left:986px;top:236px;width:197px;height:248px">
<svg width="197" height="248" viewBox="0 0 230 290" font-family="Montserrat,sans-serif">
  <text x="115" y="38" font-size="22" text-anchor="middle" fill="#333">Test Scores</text>
  <rect x="40" y="66" width="42" height="131" fill="var(--purple)"/>
  <rect x="94" y="121" width="42" height="76" fill="var(--orange)"/>
  <rect x="148" y="177" width="42" height="20" fill="var(--sky)"/>
  <g fill="#fff" font-size="12.5" font-weight="600"><text x="47" y="84">75%</text><text x="101" y="141">15%</text><text x="155" y="192">10%</text></g>
  <g font-size="11.5" font-weight="500" fill="#444">
    <rect x="19" y="233" width="4" height="13" fill="var(--purple)"/><text x="28" y="243">SECONDARY</text>
    <rect x="137" y="233" width="4" height="13" fill="var(--orange)"/><text x="146" y="244">COLLEGE</text>
    <rect x="19" y="260" width="4" height="13" fill="var(--sky)"/><text x="28" y="270">HIGHER</text>
  </g>
</svg>
</section>

<section class="abs card" style="left:771px;top:512px;width:197px;height:257px">
<svg width="197" height="257" viewBox="0 0 230 300" font-family="Montserrat,sans-serif">
  <circle cx="114" cy="76" r="60" fill="none" stroke="var(--orange)" stroke-width="2"/>
  <g fill="none" stroke="var(--orange)" stroke-width="2.2">
    <path d="M102 52h24v12a12 12 0 01-24 0z"/><path d="M102 56h-9c0 8 4 12 10 13M126 56h9c0 8-4 12-10 13"/>
    <path d="M114 76v8M106 84h16v4h-16zM103 88h22v4h-22z"/>
    <path d="M114 55l2 4 4 .5-3 3 .8 4-3.8-2-3.8 2 .8-4-3-3 4-.5z" stroke-width="1.4"/>
  </g>
  <g font-size="17" text-anchor="middle" fill="#222"><text x="115" y="186">Total Alumni</text><text x="115" y="204">Members</text></g>
  <path stroke="var(--orange)" stroke-width="3" d="M30 300V262M35 300V255M40 300V247M45 300V260M50 300V252M55 300V258M60 300V265M65 300V250M70 300V262M75 300V244M80 300V256M85 300V262M90 300V253M95 300V260M100 300V265M105 300V250M110 300V257M115 300V243M120 300V255M125 300V262M130 300V248M135 300V258M140 300V240M145 300V256M150 300V262M155 300V245M160 300V256M165 300V263M170 300V250M175 300V258M180 300V265M185 300V247M190 300V253M195 300V258M200 300V255"/>
</svg>
</section>

<section class="abs card" style="left:986px;top:512px;width:197px;height:257px">
<svg width="197" height="257" viewBox="0 0 230 300" font-family="Montserrat,sans-serif">
  <circle cx="114" cy="76" r="60" fill="none" stroke="#e6e6e6" stroke-width="2"/>
  <path d="M114 16A60 60 0 1 1 62 106" fill="none" stroke="var(--blue)" stroke-width="2.2"/>
  <g fill="none" stroke="var(--blue)" stroke-width="2.4"><circle cx="115" cy="67" r="10"/><path d="M96 97c0-10 8-15 19-15s19 5 19 15c0 3-2 4-5 4H101c-3 0-5-1-5-4z"/></g>
  <g font-size="17" text-anchor="middle" fill="#222"><text x="115" y="186">Total</text><text x="115" y="204">Admin Users</text></g>
  <path stroke="var(--blue)" stroke-width="3" d="M30 300V262M35 300V253M40 300V247M45 300V260M50 300V252M55 300V258M60 300V265M65 300V250M70 300V262M75 300V254M80 300V256M85 300V262M90 300V253M95 300V260M100 300V265M105 300V250M110 300V243M115 300V255M120 300V262M125 300V248M130 300V258M135 300V245M140 300V256M145 300V262M150 300V241M155 300V256M160 300V263M165 300V250M170 300V258M175 300V265M180 300V247M185 300V253M190 300V258M195 300V255M200 300V262"/>
</svg>
</section>

<div class="abs action" style="left:240px"><span class="ico"><svg width="30" height="30" viewBox="0 0 30 30" fill="none" stroke="#fff" stroke-width="1.6"><circle cx="6" cy="5" r="3"/><path d="M6 9v10M3 12l3 2 8-4M4 28v-9h4v9"/><rect x="11" y="7" width="16" height="11"/><path d="M19 18v4M15 28l4-6 4 6"/></svg></span>Assign to Tutoring</div>
<div class="abs action" style="left:506px"><span class="ico"><svg width="30" height="30" viewBox="0 0 30 30" fill="none" stroke="#fff" stroke-width="1.6"><rect x="12" y="2" width="14" height="9"/><circle cx="9" cy="15" r="3"/><circle cx="20" cy="17" r="3"/><path d="M3 28c0-5 3-8 6-8s6 3 6 8M14 28c0-4 3-7 6-7s6 3 6 7"/></svg></span>Meet with Counselor</div>

<div class="abs foot">Copyright © 2017 Kestrel.&nbsp; All Rights Reserved.</div>
</body>
</html>
```